"TR wanderer" Périple Transportation Company with vehicles not exceeding 9 seats. shuttle kil

Need a design full of freshness to make a trip relaxing drive, comfortable, safe, ideal for a trip with confidence. Punctuality. A positive visual impact, enter information about the company, a logo that stands out from other competitors but remains both simple and enjoyable ... Trust, punctuality, relaxing, stress. Generosity in the passenger transport service, mainly for airport shuttles between Paris and Normandy, but also any kind of distance, France and Europe, as long as there is a road we can go

Target Market(s)

Airport Shuttle Service and all distances for the companies and individuals

Industry/Entity Type

Transfer

Contact Information for Business Card

Société : TR Périple, Luc Barnier
Adresse : Rue Paul Dantier, Bâtiment KRP, 76420 Valmerville, 0672418053, l.barnier@trperiple.fr

Font styles to use
Sans Serif

Colors

Designer to choose colors to be used in the design.

Requirements
Must have
• Company Information: Name: TR Périple Rue Paul Dantier KRP Building City: 76420 Valmerville Phone: 0672418053 Email: l.barnier@trperiple.fr
Nice to have
• a card that lives with his time, good agreement with the times
Should not have
• too classic card's lack of a nursery stock, lack of alliance of colors

```html
<!DOCTYPE html>
<html lang="fr">
<head>
<meta charset="utf-8">
<title>TR Périple — Business Card</title>
<link rel="stylesheet" href="https://fonts.googleapis.com/css2?family=Arimo:wght@400;700&display=swap">
<style>
  :root {
    --navy: #22306f;
    --sky: #1e9be0;
    --ink: #1c1c1c;
    --mail: #5a1e1e;
    --paper: #ffffff;
    --backdrop: #2a2d33;
  }
  * { margin: 0; padding: 0; box-sizing: border-box; }
  html, body {
    width: 1200px; height: 960px; overflow: hidden;
    background: var(--backdrop);
    font-family: "Arimo", Arial, sans-serif;
  }
  .sheet {
    width: 1200px; height: 960px;
    display: flex; flex-direction: column;
    align-items: center; justify-content: center; gap: 40px;
  }
  .card {
    width: 700px; height: 400px;
    background: var(--paper);
    position: relative;
    overflow: hidden;
    box-shadow: 0 12px 30px rgba(0,0,0,.45);
  }
  .brand {
    display: flex; align-items: center; justify-content: center; gap: 14px;
    color: var(--navy); font-weight: 700;
  }
  .brand-mark { background: var(--navy); }
  .card-front .brand {
    position: absolute; inset: 0;
    font-size: 52px;
  }
  .card-front .brand-mark { width: 30px; height: 30px; }

  .card-back .brand {
    position: absolute; top: 60px; left: 0; right: 0;
    font-size: 46px;
  }
  .card-back .brand-mark { width: 26px; height: 26px; }

  .person {
    position: absolute; left: 150px; top: 222px; width: 230px;
    text-align: right;
  }
  .person-name { font-size: 26px; color: var(--ink); }
  .person-role { font-size: 16px; color: var(--sky); margin-top: 2px; }

  .divider {
    position: absolute; left: 405px; top: 180px;
    width: 2px; height: 110px; background: var(--ink);
  }

  .contact {
    position: absolute; left: 440px; top: 200px;
    list-style: none; font-size: 19px; color: var(--mail);
  }
  .contact li { display: flex; align-items: center; gap: 12px; margin-bottom: 8px; }
  .contact svg { width: 18px; height: 18px; flex: none; }

  .address-band {
    position: absolute; left: 0; right: 0; bottom: 0; height: 74px;
    background: var(--navy); color: var(--paper);
    display: flex; align-items: center; justify-content: center;
    font-size: 20px; letter-spacing: .3px;
  }
</style>
</head>
<body>
<main class="sheet">
  <section class="card card-front">
    <div class="brand"><span class="brand-mark"></span>TR Périple</div>
  </section>

  <section class="card card-back">
    <div class="brand"><span class="brand-mark"></span>TR Périple</div>

    <div class="person">
      <p class="person-name">Your Name here</p>
      <p class="person-role">Founder</p>
    </div>

    <span class="divider"></span>

    <ul class="contact">
      <li>
        <svg viewBox="0 0 18 18" aria-hidden="true">
          <rect width="18" height="18" rx="3" fill="#1e9be0"/>
          <path d="M5.5 4.5c.6-.4 1.2-.2 1.5.3l.9 1.5c.3.5.1 1-.3 1.3l-.6.4c.5 1.2 1.4 2.1 2.6 2.7l.4-.6c.3-.4.9-.6 1.3-.3l1.5.9c.5.3.7.9.3 1.5-.6 1-1.7 1.4-2.8 1-2.8-1-4.9-3.1-5.9-5.9-.4-1.1 0-2.2 1.1-2.8z" fill="#fff"/>
        </svg>
        <span>0672418053</span>
      </li>
      <li>
        <svg viewBox="0 0 18 18" aria-hidden="true">
          <rect width="18" height="18" rx="3" fill="#1e9be0"/>
          <rect x="4" y="5.5" width="10" height="7" fill="#fff"/>
          <path d="M4 5.5l5 4 5-4" fill="none" stroke="#1e9be0" stroke-width="1.2"/>
        </svg>
        <span>l.barnier@trperiple.fr</span>
      </li>
    </ul>

    <footer class="address-band">Rue Paul Dantier, Building KRP, Valmerville 76420</footer>
  </section>
</main>
</body>
</html>
```